CD-Cover Desig für neues Album eines Liedermacher-Duos
Zielgruppe
Wir sind ein Liedermacher-Duo und benötigen für unser neues Album mit dem Titel 'Kiesel' ein Cover.
Infos über den Themenbereich der Songs findet man hier: https://www.vorhabenwerk.de/cd-kiesel
Aufgabenstellung
Cover könnte schlicht sein... oder auch kreativ verspielt mit warmen Farben und Formen... aber nicht kitschig.
'Kiesel' im Sinne von Geborgenheit also kein verzehrendes Feuer.. eher sonnig.
Evtl. könnte man unsere beiden Hauptinstrumente (Geige und Gitarre) andeuten.
Sonst stehen auf dem Cover nur noch unsere Namen: Dorothea Lindner & Jörg Haberl

```html
<!DOCTYPE html>
<html lang="de">
<head>
<meta charset="utf-8">
<title>Kiesel – Dorothea Lindner &amp; Jörg Haberl</title>
<link rel="stylesheet" href="https://fonts.googleapis.com/css2?family=Barlow:wght@300&family=Damion&display=swap">
<style>
  :root {
    --page: #ffffff;
    --sky-deep: #c9632e;
    --sky-mid: #ec8a3e;
    --sky-light: #f3a453;
    --sun: #fffbe6;
    --dusk: #7a4a3a;
    --frame-gold: #ffd36a;
    --frame-rose: #f2c9b8;
    --name-ink: #ffffff;
    --title-ink: rgba(250, 232, 222, 0.84);
  }
  html, body {
    margin: 0;
    padding: 0;
    width: 1200px;
    height: 1200px;
    overflow: hidden;
    background: var(--page);
  }
  .cover {
    position: relative;
    width: 1200px;
    height: 1200px;
    background: var(--page);
  }
  .cover__artwork {
    position: absolute;
    left: 60px;
    top: 60px;
    width: 1080px;
    height: 1080px;
    overflow: hidden;
    background:
      radial-gradient(circle at 817px 565px, var(--sun) 0, var(--sun) 80px, #ffd66a 100px, rgba(248,170,70,0.7) 200px, rgba(240,140,60,0) 420px),
      linear-gradient(180deg, var(--sky-deep) 0%, var(--sky-mid) 35%, var(--sky-light) 55%, #e07a36 78%, var(--dusk) 100%);
  }
  .cover__frame {
    position: absolute;
    left: 82px;
    top: 82px;
    width: 1036px;
    height: 1033px;
    box-sizing: border-box;
    border: 3px solid var(--frame-gold);
    border-bottom-color: var(--frame-rose);
    pointer-events: none;
  }
  .cover__artists {
    position: absolute;
    left: 140px;
    top: 140px;
    width: 430px;
    margin: 0;
    text-align: center;
    font-family: "Barlow", "DIN Alternate", sans-serif;
    font-weight: 300;
    font-size: 46px;
    line-height: 58px;
    color: var(--name-ink);
    letter-spacing: 0.2px;
  }
  .cover__title {
    position: absolute;
    left: 52px;
    top: 600px;
    margin: 0;
    font-family: "Damion", cursive;
    font-weight: 400;
    font-size: 360px;
    line-height: 1;
    color: var(--title-ink);
    white-space: nowrap;
  }
</style>
</head>
<body>
  <main class="cover">
    <div class="cover__artwork" role="img" aria-label="Fotografie: Gräser im Gegenlicht vor tief stehender, warm leuchtender Abendsonne in Orangetönen"></div>
    <div class="cover__frame"></div>
    <p class="cover__artists">Dorothea Lindner &amp;<br>Jörg Haberl</p>
    <h1 class="cover__title">Kiesel</h1>
  </main>
</body>
</html>
```